Book Cover

Hello!
I need someone to design a book cover with the title, subtitle and one of the photos attached.

- Title: Beyond the Grey Hours - By Corwin Ashdale
- Subtitle: A Steady Handbook for finding calm and strength after hard news.

```html
<!DOCTYPE html>
<html lang="en">
<head>
<meta charset="UTF-8">
<title>Beyond the Grey Hours — Book Cover</title>
<link rel="stylesheet" href="https://fonts.googleapis.com/css2?family=Marcellus&family=Marcellus+SC&family=Oswald:wght@700&family=Nunito:ital,wght@1,900&display=swap">
<style>
  :root {
    --page: #ffffff;
    --cover: #083d4c;
    --title-gold: #f6a800;
    --ink-light: #ffffff;
    --shadow: rgba(0, 0, 0, 0.85);
    --glow: #b9dcea;
    --portrait-blue: #2a3f8a;
    --portrait-skin: #c99a86;
  }
  * { margin: 0; padding: 0; box-sizing: border-box; }
  html, body {
    width: 1200px; height: 1200px; overflow: hidden;
    background: var(--page);
  }
  .book-cover {
    position: absolute;
    left: 227px; top: 70px;
    width: 734px; height: 1038px;
    background: var(--cover);
    overflow: hidden;
  }
  .cover-photo {
    position: absolute;
    left: 60px; top: 415px;
    width: 674px; height: 623px;
    background:
      radial-gradient(ellipse 34% 40% at 62% 42%, var(--portrait-skin) 0%, rgba(201,154,134,0.6) 55%, rgba(201,154,134,0) 100%),
      radial-gradient(ellipse 70% 45% at 60% 100%, var(--portrait-blue) 0%, rgba(42,63,138,0.85) 60%, rgba(42,63,138,0) 100%),
      radial-gradient(ellipse 60% 70% at 62% 55%, var(--glow) 0%, rgba(120,170,195,0.7) 45%, rgba(8,61,76,0) 80%);
  }
  .title {
    position: absolute;
    left: 0; right: 0; top: 84px;
    text-align: center;
    font-weight: normal;
  }
  .title-lead {
    display: block;
    font-family: "Marcellus SC", serif;
    font-size: 60px;
    line-height: 1;
    letter-spacing: 1px;
    color: var(--ink-light);
    padding-left: 6px;
  }
  .title-main {
    display: block;
    margin-top: 2px;
    font-family: "Oswald", sans-serif;
    font-weight: 700;
    font-size: 86px;
    line-height: 1;
    letter-spacing: 2px;
    color: var(--title-gold);
    text-transform: uppercase;
    text-shadow: 3px 3px 0 var(--shadow);
    padding-left: 34px;
  }
  .subtitle {
    position: absolute;
    left: 0; right: 0; top: 296px;
    text-align: center;
    font-family: "Nunito", sans-serif;
    font-style: italic;
    font-weight: 900;
    font-size: 32px;
    line-height: 40px;
    color: var(--ink-light);
    padding-left: 30px;
  }
  .author {
    position: absolute;
    left: 48px; top: 955px;
    color: var(--ink-light);
    text-shadow: 3px 3px 2px var(--shadow);
    white-space: nowrap;
    line-height: 1;
  }
  .author-by {
    font-family: "Marcellus", serif;
    font-size: 40px;
    margin-right: 10px;
  }
  .author-name {
    font-family: "Marcellus SC", serif;
    font-size: 52px;
  }
</style>
</head>
<body>
  <main class="book-cover">
    <div class="cover-photo" role="img" aria-label="Portrait photo of an older man with grey hair and beard, wearing a blue jacket, looking upward, softly glowing against the background"></div>

    <h1 class="title">
      <span class="title-lead">Beyond the</span>
      <span class="title-main">Grey Hours</span>
    </h1>

    <p class="subtitle">A Steady Handbook<br>for finding calm and<br>strength after hard news.</p>

    <p class="author"><span class="author-by">by</span><span class="author-name">Corwin Ashdale</span></p>
  </main>
</body>
</html>
```